Bring me business with this creative business card

Design my new business card. I am looking for something different with an impact. People will take a look at this card & they will 1- see how different & creative I am, 2-understand what I do 3- Call me to meet me!

I make videos with a message, testimonials. I am dynamic, fun, creative & human. My new website is in construction but in the meantime you can check this old one: brightpath.ca & another one Fernquill.com & fernquill facebook page.
I make videos. sometimes with a cameraman, sometimes with my phone. As an ex Public Relations agent, the message is the most important thing for me. I want to make my clients shine! When they start with me they often remind me of a lamb, when I finish coaching them they are powerful like LIONS! That's why I need a powerful business card!

Target Market(s)

Entrepreneurs, solo entrepreneurs, small & medium companies & start ups. People i will meet while networking. People that need videos on their website & social Networks to get attention, to be visible. men & women. From 35 to 49 years old.
I am an ex Public relations agent. I used to send clients in traditional medias, now with videos they have more chances to be seen on google the new media. I do videos of the president, his team, his loyal clients saying how great the company is & expert videos like series so people can be seen for example every 1 st of every month with a short 2 minute video. Also with my 20 years in marketing & communications I can coach & give tips to anybody who needs it.
Target: anybody who would like my old website brightpath.ca & I also have another website but it will be off line soon: fernquill.com could give you ideas.

Industry/Entity Type

Communications

Contact Information for Business Card

I am in Montreal,So the business cards have to be the usual size like we have in Montreal: 9 cm x 5 cm
Details:My text: Corinne Vautrin Communication coach/Founder. "Creating Videos as unique as you" off: 514-555-0147 cell: 514-555-0183. fernquill.com
corinne@fernquill.com logo facebook, youtube, instagram

Colors
f37122

Requirements
Must have
• Dynamic, happy. Orange. Be creative in the look but NOT the shape of the card. Easy to read. Big enough to read.
Should not have
• No funny shapes: no round, no square, just the usual. I love creative but NOT on shape.

```html
<!DOCTYPE html>
<html lang="en">
<head>
<meta charset="utf-8">
<title>Fernquill – Business Card</title>
<link rel="stylesheet" href="https://fonts.googleapis.com/css2?family=Cinzel:wght@600&family=Great+Vibes&family=Montserrat:wght@400;500;700&display=swap">
<style>
  :root {
    --bg: #e4e4e4;
    --card-dark: #151515;
    --card-dark-2: #222;
    --orange: #f37122;
    --orange-deep: #e08a0c;
    --yellow: #ffd23a;
    --gold: #b8892e;
    --script: #e2562a;
    --brown: #4a1e08;
  }
  * { margin: 0; padding: 0; box-sizing: border-box; }
  html, body { width: 1200px; height: 799px; overflow: hidden; }
  body {
    background: var(--bg);
    position: relative;
    font-family: "Montserrat", sans-serif;
  }
  .card {
    position: absolute;
    width: 540px;
    height: 300px;
    box-shadow: 0 10px 30px rgba(0,0,0,0.18);
    overflow: hidden;
  }

  /* Front */
  .card-front {
    left: 90px; top: 80px;
    background: radial-gradient(ellipse at 50% 40%, var(--card-dark-2), var(--card-dark) 75%);
    color: var(--orange);
    text-align: center;
  }
  .brand-mark {
    width: 70px; height: 70px;
    border-radius: 50%;
    background: var(--orange);
    margin: 36px auto 14px;
  }
  .brand-name {
    font-family: "Cinzel", serif;
    font-weight: 600;
    font-size: 32px;
    letter-spacing: 2px;
    color: var(--orange);
    line-height: 1;
  }
  .slogan {
    font-family: "Great Vibes", cursive;
    font-size: 30px;
    color: var(--script);
    margin-top: 22px;
  }
  .front-web {
    position: absolute; left: 0; right: 0; bottom: 26px;
    display: flex; align-items: center; gap: 12px;
    font-size: 13px; font-weight: 500; letter-spacing: 1px; color: var(--orange);
  }
  .front-web::before, .front-web::after {
    content: ""; flex: 1; height: 1px; background: var(--gold);
  }

  /* Back */
  .card-back {
    left: 570px; top: 410px;
    background: linear-gradient(135deg, var(--yellow) 0%, #fbb623 45%, var(--orange-deep) 100%);
    color: var(--brown);
  }
  .card-back::after {
    content: ""; position: absolute; left: 276px; top: 0; bottom: 0; width: 1px;
    background: rgba(140,70,0,0.18);
  }
  .person {
    position: absolute; left: 26px; top: 128px; width: 244px;
  }
  .person-name {
    font-weight: 700; font-size: 22px; line-height: 1.1;
    text-transform: uppercase; white-space: nowrap;
  }
  .person-title {
    font-size: 12px; font-weight: 500; margin-top: 4px;
  }
  .social { display: flex; gap: 12px; margin-top: 10px; padding-left: 56px; }
  .social span {
    width: 18px; height: 18px; border-radius: 50%;
    border: 1.5px solid var(--brown);
  }
  .contact {
    position: absolute; left: 298px; top: 92px;
    list-style: none; display: flex; flex-direction: column; gap: 18px;
  }
  .contact li {
    display: flex; align-items: center; gap: 14px;
    font-size: 11px; font-weight: 500; text-transform: uppercase; line-height: 1.3;
  }
  .contact svg { width: 16px; height: 16px; flex: none; fill: var(--brown); }
</style>
</head>
<body>

<section class="card card-front">
  <div class="brand-mark"></div>
  <div class="brand-name">FERNQUILL</div>
  <p class="slogan">Videos That Make You Shine</p>
  <div class="front-web">WWW.FERNQUILL.COM</div>
</section>

<section class="card card-back">
  <div class="person">
    <h1 class="person-name">Corinne Vautrin</h1>
    <p class="person-title">Communication Coach/Founder</p>
    <div class="social"><span></span><span></span><span></span></div>
  </div>
  <ul class="contact">
    <li>
      <svg viewBox="0 0 16 16"><path d="M1 3h14v10H1z M1 3l7 6 7-6" fill="none" stroke="#4a1e08" stroke-width="1.6"/></svg>
      info@fernquill.com
    </li>
    <li>
      <svg viewBox="0 0 16 16"><path d="M3 1l3 3-1.5 2c1 2 3 4 5 5l2-1.5 3 3-2 2C7 14 2 9 1 3z"/></svg>
      <span>514-555-0147 (OFF)<br>514-555-0183 (CELL)</span>
    </li>
    <li>
      <svg viewBox="0 0 16 16"><circle cx="8" cy="8" r="6.5" fill="none" stroke="#4a1e08" stroke-width="1.5"/><path d="M1.5 8h13M8 1.5c-3 3.5-3 9.5 0 13M8 1.5c3 3.5 3 9.5 0 13" fill="none" stroke="#4a1e08" stroke-width="1.2"/></svg>
      www.fernquill.com
    </li>
  </ul>
</section>

</body>
</html>
```